We need a quick postcard to mail out to our alumni telling them that they are invited to vote on a new ballot of alumni officers. I purchased a 4 color picture I want to use for the front of the postcard from pixmart but I can't get it to upload. Someone can email me at Marta.finch@bvrcampus.edu and I will email them the image. The final design needs to be clean and easy to read.

Offering doctoral, master’s, baccalaureate, and associate degrees, Saint Brigid of the Vale Campus is a four-year, independent Catholic institution, providing a strong foundation in the liberal arts and continuing its highly-regarded health sciences and nursing programs.

```html
<!DOCTYPE html>
<html lang="en">
<head>
<meta charset="utf-8">
<title>Alumni Vote Postcard – Saint Brigid of the Vale Campus</title>
<link rel="stylesheet" href="https://fonts.googleapis.com/css2?family=Open+Sans:wght@400;600;700&display=swap">
<style>
  :root {
    --page-bg: #e8e5e0;
    --navy: #175a8c;
    --navy-deep: #124a76;
    --sky: #11a2df;
    --band-light: #1c90d3;
    --band-dark: #155e98;
    --white: #ffffff;
    --line-blue: #2b7fbf;
    --photo-dark: #2b2e33;
    --photo-mid: #5d636b;
    --photo-key: #2f86cf;
  }
  * { box-sizing: border-box; margin: 0; padding: 0; }
  html, body { width: 815px; height: 1200px; overflow: hidden; }
  body {
    background: var(--page-bg);
    font-family: "Open Sans", Arial, sans-serif;
    color: var(--white);
    position: relative;
  }

  /* ---------- Front of card ---------- */
  .card-front {
    position: absolute; left: 56px; top: 53px;
    width: 691px; height: 535px;
    background: var(--white);
    box-shadow: 0 2px 6px rgba(0,0,0,.25);
  }
  .front-photo {
    position: absolute; left: 0; top: 0; width: 691px; height: 395px;
    background:
      radial-gradient(ellipse 170px 110px at 430px 260px, var(--photo-key) 0%, rgba(47,134,207,0) 100%),
      linear-gradient(160deg, var(--photo-mid) 0%, var(--photo-dark) 60%, #1d1f22 100%);
  }
  .front-band {
    position: absolute; left: 0; top: 402px; width: 691px; height: 133px;
    background: linear-gradient(90deg, var(--band-light) 0%, var(--band-dark) 100%);
    display: flex; align-items: center;
  }
  .front-tagline {
    position: absolute; left: 41px; top: 44px;
    font-size: 28px; font-weight: 400; letter-spacing: .1px;
  }
  .college-mark {
    position: absolute; left: 416px; top: 28px;
    display: flex; align-items: center; gap: 12px;
  }
  .college-mark .mark-dot {
    width: 62px; height: 62px; border-radius: 50%;
    background: var(--white);
  }
  .college-mark .mark-name {
    font-size: 20px; font-weight: 600; line-height: 25px;
    color: var(--white); width: 170px;
  }

  /* ---------- Back of card ---------- */
  .card-back {
    position: absolute; left: 56px; top: 625px;
    width: 686px; height: 530px;
    background: var(--white);
    box-shadow: 0 2px 6px rgba(0,0,0,.25);
    overflow: hidden;
  }
  .back-shapes { position: absolute; left: 0; top: 0; }
  .intro-title {
    position: absolute; left: 26px; top: 22px;
    font-size: 19px; font-weight: 700;
  }
  .intro-copy {
    position: absolute; left: 26px; top: 56px; width: 470px;
    font-size: 16px; line-height: 22.5px;
  }
  .action-copy {
    position: absolute; left: 26px; top: 195px; width: 296px;
    font-size: 16px; line-height: 22.5px; text-align: justify;
  }
  .action-copy a, .contact-copy a { color: var(--white); text-decoration: underline; }
  .contact-copy {
    position: absolute; left: 26px; top: 370px; width: 300px;
    font-size: 16px; line-height: 22.5px;
  }
  .closing-call {
    position: absolute; left: 26px; top: 446px;
    font-size: 17px; font-weight: 700; line-height: 23px; letter-spacing: 1px;
    text-transform: uppercase;
  }
  .stamp-box {
    position: absolute; left: 551px; top: 35px;
    width: 98px; height: 107px;
    border: 2px solid var(--line-blue);
  }
  .address-line {
    position: absolute; left: 388px; width: 260px; height: 0;
    border-top: 2px solid var(--line-blue);
  }
  .address-line.first { top: 268px; }
  .address-line.second { top: 307px; }
  .address-line.third { top: 346px; }
</style>
</head>
<body>

  <section class="card-front">
    <div class="front-photo" role="img" aria-label="Close-up photo of a dark computer keyboard with a large blue Enter key labelled Vote"></div>
    <div class="front-band">
      <p class="front-tagline">We value your opinion.</p>
      <div class="college-mark">
        <span class="mark-dot"></span>
        <span class="mark-name">Saint Brigid of the Vale Campus</span>
      </div>
    </div>
  </section>

  <section class="card-back">
    <svg class="back-shapes" width="686" height="530" viewBox="0 0 686 530" aria-hidden="true">
      <rect x="0" y="140" width="332" height="310" fill="var(--sky)"/>
      <path d="M0 0 H516 V146 C430 150 390 172 332 174 C220 178 110 168 0 158 Z" fill="var(--navy)"/>
      <path d="M0 158 C110 168 220 178 332 174" fill="none" stroke="var(--white)" stroke-width="4"/>
      <path d="M0 438 C100 428 220 420 332 416 V530 H0 Z" fill="var(--navy)"/>
      <path d="M0 438 C100 428 220 420 332 416" fill="none" stroke="var(--white)" stroke-width="4"/>
    </svg>

    <h2 class="intro-title">Alumni:&nbsp; Please Vote!</h2>
    <p class="intro-copy">Over the past year and a half, the Alumni Association Executive Committee has been working on a major <strong>revision to the Alumni Association bylaws</strong>. The goal is a stronger and more inclusive Alumni Association.</p>

    <p class="action-copy">In order to confirm the new bylaws <strong>we need alumni approval</strong>. Go to: <a href="#">bvrcampus.edu/alumni-feedback</a> to give us your responses to the proposed bylaws and <strong>to vote</strong> on a <strong>new slate of officers</strong>.</p>

    <p class="contact-copy">Email <a href="#">AlumniAssoc@bvrcampus.edu</a> if you have questions.</p>

    <p class="closing-call">We value your opinion.<br>Vote today!</p>

    <div class="stamp-box"></div>
    <div class="address-line first"></div>
    <div class="address-line second"></div>
    <div class="address-line third"></div>
  </section>

</body>
</html>
```